A start-up named "Corvath Therapeutics" - needs a new PowerPoint design

We need a new PowerPoint Design for an early-stage start-up named "Corvath Therapeutics" seeking to disrupt the current approach towards drug discovery within aging disorders.

We would like to build on Corvath's legacy, the founder of the modern science of genetics, by employing a multidisciplinary approach, experimenting, and providing elderly patients the attention they deserve.

We have selected the suffix "therapeutics" intentionally as it stands for (a medicine) the treatment of disease; the science of healing. Alzheimer’s treatment is a huge, urgent, unmet need:
- Shift from a disease-management system to a preventive medicine system
- Focus on increasing the health span, not only the life span

Target Market(s)

Pharma/ Biotech Executives Medical Institutions Healthcare professionals (MDs, nurses, payors, pharmacists, etc.) Patients

Industry/Entity Type

Healthcare

Other font styles liked:
• Celias

Colors
0054AA
0677BA
7BADD7
CADEEF
E8F1F8
E54698
E96AAD
F1A4CE
F9D9EA
FCEFF6
A7469A
B969AE
D3A5CF
EDDBEB
F8F0F9
6B429C
8869AF
B7A5CE
E3DAEB
F3F0F8

Requirements
Must have
• - differentiate from other companies named after Corvath - differentiate from other Pharma/ Biotech companies
Nice to have
• simplicity/ minimalist logo vivid colors gradient 3D Life-Sciences inspired Simple geometry Balance
Should not have
• mascot/ emblem watermark logo animated ink style nature-inspired inventive typography artistic chaos

```html
<!DOCTYPE html>
<html lang="en">
<head>
<meta charset="utf-8">
<title>Corvath Therapeutics – Presentation Slides</title>
<link href="https://fonts.googleapis.com/css2?family=Poppins:wght@400;500;600;700&family=Archivo:wght@700;800&display=swap" rel="stylesheet">
<style>
:root{
  --plum:#7a0f4f;
  --plum-deep:#5e0b3c;
  --orange:#f0a020;
  --orange-deep:#e58a12;
  --ink:#333333;
  --body:#4a4a4a;
  --grey:#e2e2e2;
  --stage:#230a1c;
  --paper:#ffffff;
}
*{margin:0;padding:0;box-sizing:border-box}
html,body{width:1200px;height:1098px;overflow:hidden;background:var(--stage)}
.board{position:relative;width:1200px;height:1098px}
.slide{position:absolute;width:469px;height:263px;background:var(--paper);overflow:hidden;box-shadow:0 3px 10px rgba(0,0,0,.35)}
.slide svg{display:block;width:469px;height:263px}
.col-left{left:108px}.col-right{left:623px}
.row-1{top:115px}.row-2{top:417px}.row-3{top:719px}
text{font-family:'Poppins',sans-serif}
.brand{font-family:'Poppins',sans-serif;font-weight:600;fill:var(--plum)}
.heading{font-family:'Archivo',sans-serif;font-weight:800;fill:var(--ink)}
.heading-spaced{font-family:'Poppins',sans-serif;font-weight:700;fill:var(--ink);letter-spacing:2.5px}
.body{font-size:6px;fill:var(--body)}
.micro{font-size:3.6px;fill:#777}
.label{font-size:5px;fill:var(--ink);letter-spacing:.4px}
.item-title{font-size:7px;font-weight:700;fill:var(--ink)}
.band{fill:var(--plum)}
</style>
</head>
<body>
<svg width="0" height="0" style="position:absolute" aria-hidden="true">
  <defs>
    <symbol id="tick-box" viewBox="0 0 16 16">
      <rect x="1" y="3" width="12" height="12" rx="2" fill="none" stroke="#f0a020" stroke-width="1.6"/>
      <path d="M3.5 9 L7 12.5 L15 2.5" fill="none" stroke="#f0a020" stroke-width="1.8" stroke-linecap="round" stroke-linejoin="round"/>
    </symbol>
    <linearGradient id="plum-fill" x1="0" y1="0" x2="1" y2="1">
      <stop offset="0" stop-color="#8e1660"/><stop offset="1" stop-color="#5e0b3c"/>
    </linearGradient>
    <linearGradient id="orange-fill" x1="0" y1="0" x2="1" y2="1">
      <stop offset="0" stop-color="#f5ad2a"/><stop offset="1" stop-color="#e58a12"/>
    </linearGradient>
  </defs>
</svg>

<main class="board">

  <!-- Cover -->
  <section class="slide col-left row-1 slide-cover">
    <svg viewBox="0 0 469 263">
      <rect x="80" y="104" width="16" height="16" fill="var(--plum)"/>
      <text class="brand" x="106" y="120" font-size="30">Corvath Therapeutics</text>
      <rect class="band" x="0" y="201" width="469" height="24"/>
    </svg>
  </section>

  <!-- Gauges -->
  <section class="slide col-right row-1 slide-gauges">
    <svg viewBox="0 0 469 263">
      <rect class="band" x="0" y="21" width="297" height="13"/>
      <rect x="305" y="23" width="7" height="7" fill="var(--plum)"/>
      <text class="brand" x="315" y="30" font-size="8.5">Corvath Therapeutics</text>
      <rect class="band" x="420" y="21" width="49" height="13"/>

      <g class="gauges" fill="none" stroke-width="3">
        <circle cx="67" cy="94" r="17" stroke="var(--plum)" stroke-dasharray="85 22" transform="rotate(-60 67 94)"/>
        <circle cx="140" cy="94" r="17" stroke="var(--orange)" stroke-dasharray="55 52" transform="rotate(0 140 94)"/>
        <circle cx="213" cy="94" r="17" stroke="var(--plum)" stroke-dasharray="62 45" transform="rotate(-90 213 94)"/>
        <circle cx="67" cy="174" r="17" stroke="var(--plum)" stroke-dasharray="70 37" transform="rotate(150 67 174)"/>
        <circle cx="140" cy="174" r="17" stroke="var(--orange)" stroke-dasharray="55 52" transform="rotate(100 140 174)"/>
        <circle cx="213" cy="174" r="17" stroke="var(--plum)" stroke-dasharray="52 55" transform="rotate(180 213 174)"/>
      </g>
      <g font-size="7.5" fill="#555" text-anchor="middle">
        <text x="67" y="97">1.8</text><text x="140" y="97">3.5</text><text x="213" y="97">9.5</text>
        <text x="67" y="177">30%</text><text x="140" y="177">10%</text><text x="213" y="177">34%</text>
      </g>
      <g text-anchor="middle">
        <text class="label" x="67" y="125">HEADLINE</text>
        <text class="micro" x="67" y="131">Lorem ipsum dolor</text><text class="micro" x="67" y="136">sit amet consectetur</text><text class="micro" x="67" y="141">adipiscing elit, sed do</text>
        <text class="label" x="140" y="125">HEADLINE</text>
        <text class="micro" x="140" y="131">Lorem ipsum dolor</text><text class="micro" x="140" y="136">sit amet consectetur</text><text class="micro" x="140" y="141">adipiscing elit, sed do</text>
        <text class="label" x="213" y="125">HEADLINE</text>
        <text class="micro" x="213" y="131">Lorem ipsum dolor</text><text class="micro" x="213" y="136">sit amet consectetur</text><text class="micro" x="213" y="141">adipiscing elit, sed do</text>
        <text class="label" x="67" y="205">HEADLINE</text>
        <text class="micro" x="67" y="211">Lorem ipsum dolor</text><text class="micro" x="67" y="216">sit amet consectetur</text><text class="micro" x="67" y="221">adipiscing elit, sed do</text>
        <text class="label" x="140" y="205">HEADLINE</text>
        <text class="micro" x="140" y="211">Lorem ipsum dolor</text><text class="micro" x="140" y="216">sit amet consectetur</text><text class="micro" x="140" y="221">adipiscing elit, sed do</text>
        <text class="label" x="213" y="205">HEADLINE</text>
        <text class="micro" x="213" y="211">Lorem ipsum dolor</text><text class="micro" x="213" y="216">sit amet consectetur</text><text class="micro" x="213" y="221">adipiscing elit, sed do</text>
      </g>
      <g stroke="#888" stroke-width=".6">
        <line x1="103" y1="74" x2="103" y2="224"/><line x1="178" y1="74" x2="178" y2="224"/>
        <line x1="298" y1="74" x2="298" y2="224" stroke="#333" stroke-width=".9"/>
      </g>
      <text class="heading-spaced" x="304" y="90" font-size="15">Title Here</text>
      <g class="body" font-size="6">
        <text x="304" y="106">Lorem ipsum dolor sit amet,</text><text x="304" y="113">consectetur adipiscing elit. Etiam</text><text x="304" y="120">iaculis commodo.</text>
        <text x="304" y="136">Lorem ipsum dolor sit amet,</text><text x="304" y="143">consectetur adipiscing elit. Etiam</text><text x="304" y="150">iaculis commod.</text>
        <text x="304" y="174">Lorem ipsum dolor sit amet,</text><text x="304" y="181">consectetur adipiscing elit. Etiam</text><text x="304" y="188">iaculis commod.</text>
        <text x="304" y="203">Lorem ipsum dolor sit amet,</text><text x="304" y="210">consectetur adipiscing elit. Etiam</text><text x="304" y="217">iaculis commod.</text>
      </g>
    </svg>
  </section>

  <!-- Bars and ratio -->
  <section class="slide col-left row-2 slide-ratio">
    <svg viewBox="0 0 469 263">
      <rect class="band" x="0" y="21" width="317" height="13"/>
      <rect x="322" y="23" width="7" height="7" fill="var(--plum)"/>
      <text class="brand" x="332" y="30" font-size="8.3">Corvath Therapeutics</text>
      <rect class="band" x="439" y="21" width="30" height="13"/>

      <g class="body"><text x="35" y="53">Lorem ipsum dolor sit amet, consectetur</text><text x="35" y="60">adipiscing elit. Etiam iaculis commod.</text></g>
      <g fill="var(--plum)">
        <rect x="43" y="158" width="4" height="20"/><rect x="52" y="136" width="4" height="42"/>
        <rect x="61" y="114" width="4" height="64"/><rect x="70" y="86" width="4" height="92"/>
      </g>
      <g fill="var(--orange)">
        <rect x="100" y="158" width="4" height="20"/><rect x="109" y="136" width="4" height="42"/>
        <rect x="118" y="114" width="4" height="64"/><rect x="127" y="86" width="4" height="92"/>
      </g>
      <text class="body" x="35" y="189">Lorem ipsum</text><text class="body" x="92" y="189">Lorem ipsum</text>
      <circle cx="234" cy="133" r="57" fill="var(--plum)"/>
      <circle cx="234" cy="133" r="58" fill="none" stroke="#111" stroke-width="2" stroke-dasharray="270 95" transform="rotate(-88 234 133)"/>
      <text x="234" y="142" text-anchor="middle" font-size="24" font-weight="700" fill="#fff">75%</text>
      <rect x="337" y="137" width="7" height="7" fill="var(--plum)"/>
      <text class="body" x="351" y="141">Lorem ipsum dolor</text><text class="body" x="351" y="148">sit amet, co.</text>
      <rect x="337" y="169" width="7" height="7" fill="var(--orange)"/>
      <text class="body" x="351" y="173">Lorem ipsum dolor</text><text class="body" x="351" y="180">sit amet, co.</text>
      <line x1="35" y1="210" x2="434" y2="210" stroke="#555" stroke-width=".7"/>
      <g class="body" text-anchor="middle">
        <text x="234" y="221">Lorem ipsum dolor sit amet, consectetur adipiscing elit. Etiam iaculis commod. Lorem ipsum dolor sit amet,</text>
        <text x="234" y="228">consectetur adipiscing elit. Etiam iaculis commod. Lorem ipsum dolor sit amet, consectetur adipiscing elit. Etiam</text>
        <text x="234" y="235">iaculis commod.Lorem ipsum dolor sit amet, consectetur adipiscing elit. Etiam iaculis commod.</text>
      </g>
    </svg>
  </section>

  <!-- Overlap chart -->
  <section class="slide col-right row-2 slide-overlap">
    <svg viewBox="0 0 469 263">
      <rect class="band" x="0" y="21" width="317" height="13"/>
      <rect x="322" y="23" width="7" height="7" fill="var(--plum)"/>
      <text class="brand" x="332" y="30" font-size="8.3">Corvath Therapeutics</text>
      <rect class="band" x="439" y="21" width="30" height="13"/>

      <text class="heading" x="34" y="91" font-size="17">TITLE HERE</text>
      <g class="checklist">
        <use href="#tick-box" x="34" y="102" width="16" height="16"/>
        <use href="#tick-box" x="34" y="128" width="16" height="16"/>
        <use href="#tick-box" x="34" y="154" width="16" height="16"/>
        <use href="#tick-box" x="34" y="180" width="16" height="16"/>
      </g>
      <g class="body" font-size="5.5">
        <text x="59" y="108">Lorem ipsum dolor sit amet,</text><text x="59" y="114">consectetur adipiscing elit.</text><text x="59" y="120">Etiam iaculis commodo.</text>
        <text x="59" y="134">Lorem ipsum dolor sit amet,</text><text x="59" y="140">consectetur adipiscing elit.</text><text x="59" y="146">Etiam iaculis commod.</text>
        <text x="59" y="160">Lorem ipsum dolor sit amet,</text><text x="59" y="166">consectetur adipiscing elit.</text><text x="59" y="172">Etiam iaculis commod.</text>
        <text x="59" y="186">Lorem ipsum dolor sit amet,</text><text x="59" y="192">consectetur adipiscing elit.</text><text x="59" y="198">Etiam iaculis commod.</text>
      </g>
      <circle cx="348" cy="129" r="42" fill="url(#orange-fill)"/>
      <circle cx="306" cy="157" r="42" fill="url(#orange-fill)" opacity=".95"/>
      <circle cx="285" cy="111" r="41" fill="url(#plum-fill)" opacity=".9"/>
      <g fill="none" stroke="#fff" stroke-width="1">
        <path d="M278 96 h9 l4 4 v14 h-13 z M282 110 l4 -4 l2 2 l3 -4"/>
        <path d="M337 125 h18 v11 h-18 z M343 140 h6 M346 136 v4"/>
        <path d="M298 155 h16 v16 h-16 z M302 155 v-3 a4 4 0 0 1 8 0 v3"/>
      </g>
      <text x="357" y="82" font-size="11" font-weight="700" fill="var(--plum)">32%</text>
      <text class="micro" x="387" y="75" font-size="4.5">Lorem ipsum dolor</text><text class="micro" x="387" y="81" font-size="4.5">sit amet consectetur</text>
      <path d="M366 94 v6 l-12 12" fill="none" stroke="#444" stroke-width=".5"/>
      <text x="235" y="160" font-size="11" font-weight="700" fill="var(--plum)">21%</text>
      <text class="micro" x="230" y="153" font-size="4.5" text-anchor="end">Lorem ipsum dolor</text><text class="micro" x="230" y="159" font-size="4.5" text-anchor="end">sit amet consectetur</text>
      <path d="M218 134 h26 l8 -6" fill="none" stroke="#444" stroke-width=".5"/>
      <text x="352" y="190" font-size="11" font-weight="700" fill="var(--plum)">45%</text>
      <text class="micro" x="384" y="184" font-size="4.5">Lorem ipsum dolor</text><text class="micro" x="384" y="190" font-size="4.5">sit amet consectetur</text>
      <path d="M326 197 l12 8 h12" fill="none" stroke="#444" stroke-width=".5"/>
      <rect x="222" y="218" width="10" height="10" fill="var(--plum)"/>
      <text class="micro" x="237" y="222" font-size="4.5">Lorem ipsum</text><text class="micro" x="237" y="228" font-size="4.5">dolor sit</text>
      <rect x="290" y="218" width="10" height="10" fill="var(--orange-deep)"/>
      <text class="micro" x="305" y="222" font-size="4.5">Lorem ipsum</text><text class="micro" x="305" y="228" font-size="4.5">dolor sit</text>
      <rect x="359" y="218" width="10" height="10" fill="var(--orange)"/>
      <text class="micro" x="374" y="222" font-size="4.5">Lorem ipsum</text><text class="micro" x="374" y="228" font-size="4.5">dolor sit</text>
    </svg>
  </section>

  <!-- Market opportunities -->
  <section class="slide col-left row-3 slide-market">
    <svg viewBox="0 0 469 263">
      <rect class="band" x="0" y="21" width="317" height="13"/>
      <rect x="322" y="23" width="7" height="7" fill="var(--plum)"/>
      <text class="brand" x="332" y="30" font-size="8.3">Corvath Therapeutics</text>
      <rect class="band" x="439" y="21" width="30" height="13"/>

      <g class="donut">
        <path d="M18 42 A107 107 0 0 1 55 49 L35 104 A48 48 0 0 0 18 101 Z" fill="var(--orange)"/>
        <path d="M-89 149 A107 107 0 0 1 18 42 L18 101 A48 48 0 0 0 -30 149 Z" fill="var(--orange)"/>
        <path d="M55 49 A107 107 0 1 1 -89 149 L-30 149 A48 48 0 1 0 35 104 Z" fill="var(--plum)"/>
        <circle cx="18" cy="149" r="10" fill="var(--plum)"/>
      </g>
      <g fill="none" stroke="#fff" stroke-width="1.1">
        <path d="M14 74 h10 l-2 -4 h-6 z M12 78 a7 7 0 0 0 14 0 a7 7 0 0 0 -14 0"/>
        <path d="M65 90 v-5 h3 v5 M70 90 v-8 h3 v8 M75 90 v-12 h3 v12 M63 90 h18"/>
        <circle cx="93" cy="147" r="7"/><circle cx="93" cy="147" r="3.5"/><path d="M93 147 l8 -8"/>
        <ellipse cx="72" cy="203" rx="5" ry="2"/><ellipse cx="72" cy="207" rx="5" ry="2"/><ellipse cx="72" cy="211" rx="5" ry="2"/>
        <circle cx="13" cy="227" r="3"/><circle cx="22" cy="227" r="3"/><path d="M7 236 a6 5 0 0 1 12 0 M16 236 a6 5 0 0 1 12 0"/>
      </g>
      <text class="heading" x="201" y="80" font-size="17">MARKET OPPORTUNITIES</text>
      <g fill="none" stroke="var(--plum)" stroke-width="1.1">
        <path d="M208 88 h8 l-2 -3 h-4 z M206 95 a6 6 0 0 0 12 0 a6 6 0 0 0 -12 0"/>
        <path d="M207 134 v-5 h3 v5 M212 134 v-8 h3 v8 M217 134 v-12 h3 v12 M205 134 h17"/>
        <circle cx="213" cy="163" r="6"/><circle cx="213" cy="163" r="3"/><path d="M213 163 l7 -7"/>
        <ellipse cx="215" cy="190" rx="5" ry="2"/><ellipse cx="215" cy="194" rx="5" ry="2"/><ellipse cx="215" cy="198" rx="5" ry="2"/><circle cx="209" cy="200" r="4"/>
        <circle cx="210" cy="222" r="3"/><circle cx="219" cy="222" r="3"/><path d="M204 231 a6 5 0 0 1 12 0 M213 231 a6 5 0 0 1 12 0"/>
      </g>
      <g class="body" font-size="5.7">
        <text class="item-title" x="234" y="96">TITLE</text>
        <text x="234" y="103">It is a process to allow an organization to focus resources on</text>
        <text x="234" y="110">the greatest opportunities to increase sales and achieve the</text>
        <text x="234" y="117">company's target.</text>
        <text class="item-title" x="234" y="137">TITLE</text>
        <text x="234" y="144">Research your target group and narrow your market.</text>
        <text class="item-title" x="234" y="163">TITLE</text>
        <text x="234" y="170">Your brand identity is a way to tell your brand story and</text>
        <text x="234" y="177">position yourself from your competitors visually.</text>
        <text class="item-title" x="234" y="194">TITLE</text>
        <text x="234" y="201">Marketing strategy's objective is to increase sales and gain a</text>
        <text x="234" y="208">competitive advantage over other competitors.</text>
        <text class="item-title" x="234" y="226">TITLE</text>
        <text x="234" y="233">A new way of how we purchase goods at fingertips in</text>
        <text x="234" y="240">modern era.</text>
      </g>
      <g stroke="#555" stroke-width=".5">
        <line x1="204" y1="124" x2="430" y2="124"/><line x1="204" y1="150" x2="430" y2="150"/>
        <line x1="204" y1="182" x2="430" y2="182"/><line x1="204" y1="213" x2="430" y2="213"/>
      </g>
    </svg>
  </section>

  <!-- Rings and steps -->
  <section class="slide col-right row-3 slide-steps">
    <svg viewBox="0 0 469 263">
      <rect class="band" x="0" y="21" width="317" height="13"/>
      <rect x="322" y="23" width="7" height="7" fill="var(--plum)"/>
      <text class="brand" x="332" y="30" font-size="8.3">Corvath Therapeutics</text>
      <rect class="band" x="439" y="21" width="30" height="13"/>

      <g fill="none" stroke="var(--grey)" stroke-width="2.5">
        <circle cx="95" cy="149" r="72"/><circle cx="95" cy="149" r="59"/><circle cx="95" cy="149" r="45"/><circle cx="95" cy="149" r="32"/>
      </g>
      <g fill="none" stroke="var(--plum)" stroke-width="2.5">
        <circle cx="95" cy="149" r="72" stroke-dasharray="330 123" transform="rotate(-90 95 149)"/>
        <circle cx="95" cy="149" r="59" stroke-dasharray="230 141" transform="rotate(-90 95 149)"/>
        <circle cx="95" cy="149" r="45" stroke-dasharray="160 123" transform="rotate(-90 95 149)"/>
        <circle cx="95" cy="149" r="32" stroke-dasharray="90 111" transform="rotate(-90 95 149)"/>
      </g>
      <circle cx="198" cy="89" r="15" fill="url(#plum-fill)"/>
      <circle cx="198" cy="127" r="15" fill="url(#plum-fill)"/>
      <circle cx="198" cy="166" r="15" fill="url(#orange-fill)"/>
      <circle cx="198" cy="204" r="15" fill="url(#orange-fill)"/>
      <g font-size="11" font-weight="500" fill="var(--ink)">
        <text x="229" y="83">01</text><text x="229" y="121">02</text><text x="229" y="160">03</text><text x="229" y="198">04</text>
      </g>
      <g class="micro" font-size="4.3">
        <text x="229" y="89">Lorem ipsum dolor</text><text x="229" y="95">sit amet consectetur</text><text x="229" y="101">adipiscing elit, sed do</text>
        <text x="229" y="127">Lorem ipsum dolor</text><text x="229" y="133">sit amet consectetur</text><text x="229" y="139">adipiscing elit, sed do</text>
        <text x="229" y="166">Lorem ipsum dolor</text><text x="229" y="172">sit amet consectetur</text><text x="229" y="178">adipiscing elit, sed do</text>
        <text x="229" y="204">Lorem ipsum dolor</text><text x="229" y="210">sit amet consectetur</text><text x="229" y="216">adipiscing elit, sed do</text>
      </g>
      <text class="heading" x="315" y="92" font-size="17">TITLE HERE</text>
      <g>
        <use href="#tick-box" x="322" y="107" width="18" height="18"/>
        <use href="#tick-box" x="322" y="138" width="18" height="18"/>
        <use href="#tick-box" x="322" y="169" width="18" height="18"/>
        <use href="#tick-box" x="322" y="200" width="18" height="18"/>
      </g>
      <g class="body" font-size="5.8">
        <text x="345" y="113">Lorem ipsum dolor sit amet,</text><text x="345" y="119">consectetur adipiscing elit.</text><text x="345" y="125">Etiam iaculis commodo.</text>
        <text x="345" y="144">Lorem ipsum dolor sit amet,</text><text x="345" y="150">consectetur adipiscing elit.</text><text x="345" y="156">Etiam iaculis commod.</text>
        <text x="345" y="175">Lorem ipsum dolor sit amet,</text><text x="345" y="181">consectetur adipiscing elit.</text><text x="345" y="187">Etiam iaculis commod.</text>
        <text x="345" y="206">Lorem ipsum dolor sit amet,</text><text x="345" y="212">consectetur adipiscing elit.</text><text x="345" y="218">Etiam iaculis commod.</text>
      </g>
    </svg>
  </section>

</main>
</body>
</html>
```